SilverLedgerOak - Double Sided Business Card

We are looking for design options or our business cards. We are a Business Solutions and HR solutions Provider - the theme is business, for this card.

Our brand colours are represented within our logo.

Details needed to be put on the front of the business card are:

Employees name: [Sample Name]
Role: [Sample Role]

Address: Suite 4 - Level 3/48 Halloran Avenue Parramatta NSW 2150
M: 0000 000 000
P: 1300 847 213
F: 1300 847 286
E: sample@silverledgeroak.com.au
www.silverledgeroak.com.au
Updates

Reason: Hello, could we please increase our deadline by 5 days. Thanking you, Tess

Target Market(s)

Business Owners, also Candidates looking for Employment

Industry/Entity Type

Business

Contact Information for Business Card

Role: [Sample Role]

M: 0000 000 000
P: 1300 847 213
F: 1300 847 286

Font styles to use
Sans Serif

Colors
3276b5
3176b5
0455a3
85abd2
cfdeed
ffffff
000000
1b1b1b
757575

Requirements
Must have
• Details needed to be put on the front of the business card are:
• Employees name: [Sample Name]
• Role: [Sample Role]
• Address: Suite 4 - Level 3/48 Halloran Avenue Parramatta NSW 2150
• M: 0000 000 000
• P: 1300 847 213
• F: 1300 847 286
• E: sample@silverledgeroak.com.au
• www.silverledgeroak.com.au
Nice to have
• Simplicity, clean and professional.

```html
<!DOCTYPE html>
<html lang="en">
<head>
<meta charset="utf-8">
<title>SilverLedgerOak – Business Card</title>
<link rel="stylesheet" href="https://fonts.googleapis.com/css2?family=Source+Sans+3:wght@400;600;700&display=swap">
<style>
  :root {
    --stage: #262626;
    --card-light: #ebebeb;
    --card-light-edge: #dcdcdc;
    --card-dark: #1b1b1b;
    --navy: #1c2b4d;
    --brand-blue: #3176b5;
    --deep-blue: #0455a3;
    --soft-blue: #85abd2;
    --ink: #1b1b1b;
    --muted: #757575;
    --white: #ffffff;
  }
  * { box-sizing: border-box; margin: 0; padding: 0; }
  html, body {
    width: 1200px; height: 600px; overflow: hidden;
    background: var(--stage);
    font-family: "Source Sans 3", "Helvetica Neue", Arial, sans-serif;
  }
  .canvas {
    position: relative; width: 1200px; height: 600px;
    display: flex; align-items: center; justify-content: center; gap: 26px;
  }
  .card {
    position: relative; width: 466px; height: 272px;
    border-radius: 18px; overflow: hidden;
  }

  /* Front */
  .card--front {
    background: linear-gradient(135deg, var(--card-light) 0%, var(--card-light-edge) 100%);
  }
  .brand-mark {
    position: absolute; left: 30px; top: 124px;
    display: flex; align-items: center; gap: 8px;
  }
  .brand-mark__square { width: 22px; height: 22px; background: var(--navy); }
  .brand-mark__name {
    font-size: 18px; font-weight: 600; color: var(--navy); letter-spacing: 0.2px;
  }
  .details {
    position: absolute; left: 220px; top: 52px; color: var(--ink);
  }
  .details__name {
    font-size: 19px; font-weight: 400; color: var(--navy); line-height: 1.1;
  }
  .details__role {
    font-size: 12.5px; color: var(--brand-blue); margin-top: 1px;
  }
  .contact-list { list-style: none; margin-top: 16px; }
  .contact-list li {
    display: flex; align-items: flex-start; gap: 8px;
    font-size: 12.5px; line-height: 1.3; margin-bottom: 7px;
  }
  .contact-list svg { flex: none; width: 11px; height: 11px; margin-top: 2px; fill: var(--navy); }

  /* Back */
  .card--back {
    background: linear-gradient(135deg, #202020 0%, var(--card-dark) 60%, #161616 100%);
    display: flex; flex-direction: column; align-items: center;
  }
  .back-mark {
    margin-top: 104px;
    display: flex; align-items: center; gap: 10px;
  }
  .back-mark__square { width: 30px; height: 30px; background: var(--brand-blue); }
  .back-mark__name {
    font-size: 30px; font-weight: 700; color: var(--brand-blue); letter-spacing: 0.5px;
  }
  .back-rule {
    width: 240px; height: 1px; background: var(--muted); margin-top: 10px;
  }
  .tagline {
    margin-top: 8px; font-size: 10px; font-weight: 700; color: var(--white);
  }
  .web {
    margin-top: 18px; font-size: 13px; color: var(--brand-blue);
  }
</style>
</head>
<body>
<main class="canvas">
  <section class="card card--front" aria-label="Business card front">
    <div class="brand-mark">
      <span class="brand-mark__square"></span>
      <span class="brand-mark__name">SilverLedgerOak</span>
    </div>
    <div class="details">
      <p class="details__name">Your Name</p>
      <p class="details__role">Job Title</p>
      <ul class="contact-list">
        <li>
          <svg viewBox="0 0 12 12" aria-hidden="true"><path d="M3.5 0h5a1 1 0 0 1 1 1v10a1 1 0 0 1-1 1h-5a1 1 0 0 1-1-1V1a1 1 0 0 1 1-1zm0 1.5v8h5v-8zM6 10a.6.6 0 1 0 0 1.2A.6.6 0 0 0 6 10z"/></svg>
          <span>0000 000 000</span>
        </li>
        <li>
          <svg viewBox="0 0 12 12" aria-hidden="true"><path d="M0 4.5C0 2.5 3 1.5 6 1.5s6 1 6 3v1H9V4.2H3v1.3H0zM2 6.5h8l1.5 4.5h-11zM6 7.5a1.3 1.3 0 1 0 0 2.6 1.3 1.3 0 0 0 0-2.6z"/></svg>
          <span>1300 847 213</span>
        </li>
        <li>
          <svg viewBox="0 0 12 12" aria-hidden="true"><path d="M3 0h6v4H3zM1 4.5h10a1 1 0 0 1 1 1V11a1 1 0 0 1-1 1H1a1 1 0 0 1-1-1V5.5a1 1 0 0 1 1-1zm1.5 2v1h3v-1zm0 2v1h3v-1zm5-2v3h2v-3z"/></svg>
          <span>1300 847 286</span>
        </li>
        <li>
          <svg viewBox="0 0 12 12" aria-hidden="true"><path d="M0 2h12v1L6 7 0 3zM0 4.2l6 4 6-4V10H0z"/></svg>
          <span>sample@silverledgeroak.com.au</span>
        </li>
        <li>
          <svg viewBox="0 0 12 12" aria-hidden="true"><path d="M6 0a4 4 0 0 1 4 4c0 3-4 8-4 8S2 7 2 4a4 4 0 0 1 4-4zm0 2.5a1.5 1.5 0 1 0 0 3 1.5 1.5 0 0 0 0-3z"/></svg>
          <span>Suite 4 - Level 3/48 Halloran Avenue<br>Parramatta NSW 2150</span>
        </li>
      </ul>
    </div>
  </section>

  <section class="card card--back" aria-label="Business card back">
    <div class="back-mark">
      <span class="back-mark__square"></span>
      <span class="back-mark__name">SilverLedgerOak</span>
    </div>
    <div class="back-rule"></div>
    <p class="tagline">Guiding growing businesses toward clear, steady results</p>
    <p class="web">www.silverledgeroak.com.au</p>
  </section>
</main>
</body>
</html>
```